Martin Hale PA Card Logo

Current logo attached. Its 25 year old logo I have used. Looking for a new fresh elegant professional look/design for a law firm that has high net worth clientele and is estate planning business law firm. Firm mis in Palm Beach Florida.
One sided card linen stock white will be used. Logo section name section. Logo should include nice elegant design using the letter "M" perhapa (I am not wed to current font of the M on current logo.) Be creative there with logo design. My initials are MH.......color scheme I figure 3 tone... Raised Gold Foil, Blue name of firm = Martin Hale, P.A. My practice focus is Family and Business Asset Protection. My name is Martin M. Hale, Esq. Practice specialties include Asset Protection trusts, Business Succession Planning, LLC law, Estate Planning, Medicaid Planning (Maybe put those topics in bullets in a section of card. Bottom of card can be reserved smaller print address phone website and email address. Address section is not as important as logo and topics of practice on front. I foresee address section can be in dark blue. MY name and Topics dark blue as well.
Target Market(s)
affluent; business owners executives; wealth 2-10 million net worth
Industry/Entity Type
business law and estate planning
Contact Information for Business Card
White thick linen one sided

```html
<!DOCTYPE html>
<html lang="en">
<head>
<meta charset="UTF-8">
<title>Martin Hale, P.A. – Business Card</title>
<link href="https://fonts.googleapis.com/css2?family=Cinzel:wght@400;600&family=Arimo:wght@400&display=swap" rel="stylesheet">
<style>
  :root {
    --stage: #2b2b2b;
    --navy: #0f3563;
    --navy-deep: #0a2a52;
    --navy-text: #183a6b;
    --gold: #d9962a;
    --gold-soft: #e6a941;
    --white: #ffffff;
    --paper: #fdfdfd;
    --ink: #1d2f55;
  }
  * { box-sizing: border-box; margin: 0; padding: 0; }
  html, body { width: 1200px; height: 800px; overflow: hidden; }
  body { background: var(--stage); position: relative; font-family: 'Cinzel', serif; }

  .card {
    position: absolute;
    top: 245px;
    width: 540px;
    height: 310px;
    border-radius: 16px;
    overflow: hidden;
  }
  .card--front { left: 40px; }
  .card--back { left: 620px; background: var(--paper); }

  .card__pattern {
    position: absolute; inset: 0;
    background: radial-gradient(ellipse at 80% 15%, #2a4a78 0%, var(--navy) 45%, var(--navy-deep) 100%);
  }

  .lockup { position: absolute; display: flex; align-items: center; }
  .lockup__mark { border-radius: 50%; background: var(--gold); flex: none; }
  .lockup__text { display: flex; flex-direction: column; }
  .lockup__name { font-weight: 400; letter-spacing: 1px; white-space: nowrap; }
  .lockup__rule { height: 2px; background: var(--gold); margin: 4px 0 5px; }
  .lockup__role { letter-spacing: 1.5px; white-space: nowrap; }

  .card--front .lockup { left: 48px; top: 78px; }
  .card--front .lockup__mark { width: 54px; height: 54px; margin-right: 18px; }
  .card--front .lockup__name { color: var(--white); font-size: 31px; }
  .card--front .lockup__role { color: var(--white); font-size: 21px; padding-left: 40px; }

  .practice {
    position: absolute; left: 48px; right: 30px; bottom: 52px;
    color: var(--white); font-size: 13.5px; letter-spacing: .6px; line-height: 2;
    list-style: none;
  }
  .practice__row { display: flex; gap: 14px; align-items: center; white-space: nowrap; }
  .practice__dot { width: 7px; height: 7px; border-radius: 50%; background: var(--gold); flex: none; }

  .card--back .lockup--primary { left: 40px; top: 48px; }
  .card--back .lockup--primary .lockup__mark { width: 40px; height: 40px; margin-right: 12px; }
  .card--back .lockup--primary .lockup__name { color: var(--navy-text); font-size: 21px; }
  .card--back .lockup--primary .lockup__role { color: var(--navy-text); font-size: 15px; padding-left: 28px; }

  .card--back .lockup--secondary { left: 48px; top: 168px; }
  .card--back .lockup--secondary .lockup__name { color: var(--navy-text); font-size: 19px; }
  .card--back .lockup--secondary .lockup__role { color: var(--gold); font-size: 13px; padding-left: 78px; margin-top: 2px; }

  .divider { position: absolute; left: 300px; top: 118px; width: 1px; height: 74px; background: var(--gold); }

  .contacts { position: absolute; left: 318px; top: 118px; list-style: none; font-family: 'Arimo', sans-serif; font-size: 14px; color: var(--ink); }
  .contacts__item { display: flex; align-items: center; gap: 10px; height: 25px; }
  .contacts__icon { width: 16px; height: 16px; border-radius: 3px; background: var(--gold-soft); display: flex; align-items: center; justify-content: center; }

  .address-rule { position: absolute; left: 40px; right: 40px; bottom: 54px; height: 1px; background: var(--gold); }
  .address { position: absolute; left: 44px; bottom: 22px; display: flex; align-items: center; gap: 8px; font-family: 'Arimo', sans-serif; font-size: 15px; color: var(--ink); }
</style>
</head>
<body>

  <section class="card card--front" aria-label="Card front">
    <div class="card__pattern" role="img" aria-label="Navy background with a repeating embossed monogram pattern"></div>
    <div class="lockup">
      <span class="lockup__mark"></span>
      <div class="lockup__text">
        <span class="lockup__name">MARTIN HALE, P.A.</span>
        <span class="lockup__rule"></span>
        <span class="lockup__role">ELDER LAW ATTORNEY</span>
      </div>
    </div>
    <ul class="practice">
      <li class="practice__row">Asset Protection Trusts <span class="practice__dot"></span> Business Succession Planning</li>
      <li class="practice__row">LLC Law <span class="practice__dot"></span> Estate Planning <span class="practice__dot"></span> Medicaid Planning</li>
    </ul>
  </section>

  <section class="card card--back" aria-label="Card back">
    <div class="lockup lockup--primary">
      <span class="lockup__mark"></span>
      <div class="lockup__text">
        <span class="lockup__name">MARTIN HALE, P.A.</span>
        <span class="lockup__rule"></span>
        <span class="lockup__role">ELDER LAW ATTORNEY</span>
      </div>
    </div>

    <div class="lockup lockup--secondary">
      <div class="lockup__text">
        <span class="lockup__name">MARTIN HALE, P.A.</span>
        <span class="lockup__role">LAW ATTORNEY</span>
      </div>
    </div>

    <span class="divider"></span>

    <ul class="contacts">
      <li class="contacts__item">
        <span class="contacts__icon"><svg width="10" height="10" viewBox="0 0 10 10"><path d="M2 1h2l1 2-1.2 1a5 5 0 0 0 2.2 2.2L7 5l2 1v2a1 1 0 0 1-1 1A7 7 0 0 1 1 2a1 1 0 0 1 1-1z" fill="#fff"/></svg></span>
        561-555 204 318
      </li>
      <li class="contacts__item">
        <span class="contacts__icon"><svg width="10" height="10" viewBox="0 0 10 10"><path d="M1 5 9 1 6 9 5 5.5z" fill="#fff"/></svg></span>
        office@halelawpa.com
      </li>
      <li class="contacts__item">
        <span class="contacts__icon"><svg width="10" height="10" viewBox="0 0 10 10"><circle cx="5" cy="5" r="3.8" fill="none" stroke="#fff" stroke-width="1"/><path d="M1.2 5h7.6M5 1.2c-2 2.4-2 5.2 0 7.6M5 1.2c2 2.4 2 5.2 0 7.6" fill="none" stroke="#fff" stroke-width=".8"/></svg></span>
        www.halelawpa.com
      </li>
    </ul>

    <span class="address-rule"></span>
    <p class="address">
      <svg width="11" height="15" viewBox="0 0 11 15"><path d="M5.5 0A5.5 5.5 0 0 0 0 5.5C0 9.5 5.5 15 5.5 15S11 9.5 11 5.5A5.5 5.5 0 0 0 5.5 0zm0 7.7a2.2 2.2 0 1 1 0-4.4 2.2 2.2 0 0 1 0 4.4z" fill="var(--gold)"/></svg>
      4470 Royal Palm Way, 210-B, FL 33480
    </p>
  </section>

</body>
</html>
```